Business Card - Professional Minimalist - Double sided

We appreciate minimalist logo/web/collateral designs that allow design to tell a story. We want to relay a professional image/approach but throwing in a splash of modern when we’re able so long as it’s not distracting. Think 75% classic corporate, 25% modern. Open to black or white design, not sure which might look the best.

Target Market(s)

Senior executives or related government affairs contacts within the agriculture, energy, and defense industries (i.e., potential clients) but located outside of Washington, DC. Most potential clients based in DC with be familiar with both of us and our shared history.

Industry/Entity Type

Consulting

Contact Information for Business Card

Name: Daniel R. Whitlock
Title: Co-Founder & Partner
Address: 418 Bramblewood Ave. SE | Suite 2716 | Washington, D.C. 20019
Phone: (202) 555-0187
Email: Daniel@HollerbyWhitlock.com

Font styles to use
Serif

Colors

Designer to choose only greyscale colors for use in the design.

Requirements
Must have
• Name: Daniel R. Whitlock
Phone: (202) 555-0187

```html
<!DOCTYPE html>
<html lang="en">
<head>
<meta charset="UTF-8">
<title>Hollerby Whitlock Group — Business Card</title>
<link href="https://fonts.googleapis.com/css2?family=Cinzel:wght@500&family=Open+Sans:wght@400;700&display=swap" rel="stylesheet">
<style>
  :root {
    --backdrop: #2a2a2a;
    --card-light: #ffffff;
    --card-dark: #1d1b1c;
    --brand-ink-light: #4a4a4a;
    --brand-ink-dark: #8c8c8c;
    --name-ink: #6f6f6f;
    --text-ink: #a9a9a9;
    --divider: #3a3839;
  }
  * { margin: 0; padding: 0; box-sizing: border-box; }
  html, body {
    width: 1200px; height: 900px; overflow: hidden;
    background: var(--backdrop);
  }
  .canvas {
    position: relative; width: 1200px; height: 900px;
  }
  .card {
    position: absolute; left: 250px; width: 700px; height: 400px;
    box-shadow: 0 10px 24px rgba(0,0,0,0.45);
  }
  .card--front { top: 40px; background: var(--card-light); }
  .card--back { top: 460px; background: var(--card-dark); }

  .brand {
    position: absolute; display: flex; align-items: center; gap: 14px;
    font-family: "Cinzel", serif; font-weight: 500;
    font-size: 27px; letter-spacing: 0.5px; white-space: nowrap;
  }
  .brand__square {
    width: 40px; height: 40px; border: 3px solid currentColor; flex: none;
  }
  .card--front .brand {
    left: 50%; top: 50%; transform: translate(-50%, -50%);
    color: var(--brand-ink-light);
  }
  .card--back .brand {
    left: 40px; top: 50%; transform: translateY(-50%);
    font-size: 18px; letter-spacing: 0; gap: 10px;
    color: var(--brand-ink-dark);
  }
  .card--back .brand__square { width: 26px; height: 26px; border-width: 2px; }

  .card__divider {
    position: absolute; left: 395px; top: 40px; width: 1px; height: 320px;
    background: var(--divider);
  }
  .contact {
    position: absolute; left: 420px; top: 70px; right: 24px;
    font-family: "Open Sans", sans-serif; color: var(--text-ink);
  }
  .contact__name {
    font-weight: 700; font-size: 21px; letter-spacing: 0.5px;
    text-transform: uppercase; color: var(--name-ink); line-height: 1.1;
  }
  .contact__title {
    font-size: 13px; text-transform: uppercase; margin-bottom: 18px;
  }
  .contact__list { list-style: none; font-size: 13px; line-height: 1.7; }
  .contact__list li { display: flex; align-items: center; gap: 8px; }
  .contact__list svg { width: 13px; height: 13px; flex: none; }
  .contact__address {
    font-size: 13px; line-height: 1.5; margin-top: 18px;
  }
</style>
</head>
<body>
<main class="canvas">
  <section class="card card--front" aria-label="Card front">
    <div class="brand"><span class="brand__square"></span>Hollerby Whitlock Group</div>
  </section>

  <section class="card card--back" aria-label="Card back">
    <div class="brand"><span class="brand__square"></span>Hollerby Whitlock Group</div>
    <div class="card__divider"></div>
    <div class="contact">
      <h1 class="contact__name">Daniel R. Whitlock</h1>
      <p class="contact__title">Co-Founder &amp; Partner</p>
      <ul class="contact__list">
        <li>
          <svg viewBox="0 0 16 16" aria-hidden="true"><path d="M3 1.5l2.5 0 1 3.5-1.6 1.2a8 8 0 0 0 4.9 4.9l1.2-1.6 3.5 1v2.5c0 .8-.7 1.5-1.5 1.5A12.5 12.5 0 0 1 1.5 3c0-.8.7-1.5 1.5-1.5z" fill="none" stroke="currentColor" stroke-width="1.4"/></svg>
          (202) 555-0187
        </li>
        <li>
          <svg viewBox="0 0 16 16" aria-hidden="true"><rect x="1" y="3" width="14" height="10" fill="currentColor"/><path d="M1 3l7 6 7-6" fill="none" stroke="var(--card-dark)" stroke-width="1.2"/></svg>
          Daniel@HollerbyWhitlock.com
        </li>
        <li>
          <svg viewBox="0 0 16 16" aria-hidden="true"><g fill="none" stroke="currentColor" stroke-width="1.2"><circle cx="8" cy="8" r="6.5"/><ellipse cx="8" cy="8" rx="3" ry="6.5"/><path d="M1.5 8h13M2.5 4.8h11M2.5 11.2h11"/></g></svg>
          www.HollerbyWhitlock.com
        </li>
      </ul>
      <p class="contact__address">418 Bramblewood Ave. SE | Suite<br>2716 | Washington, D.C. 20019</p>
    </div>
  </section>
</main>
</body>
</html>
```